Verostel business card

Business card for sustainable investment company called "Verostel". Verostel is an exchange platform selling carbon credits between buyers and sellers. Carbon Credits are an environmental commodity for reducing global carbon emissions.

the card should obviously have our logo and the theme should be sustainability/environment mixed with a trading platform.

Contact Information for Business Card

Logo, Name, Title, Phone, Email

Colors
0054AA
0677BA
7BADD7
CADEEF
E8F1F8
0094D4
00A9DD
6FCCEA
C7EBF8
E9F6FB
00AB8E
00BBA5
67D7C9
C6EFE9
E9F9F6
59FF00
82FF00
B8FF75
E3FFCB
F4FFEA

```html
<!DOCTYPE html>
<html lang="en">
<head>
<meta charset="UTF-8">
<title>Verostel business card</title>
<link href="https://fonts.googleapis.com/css2?family=Lexend:wght@400;500;600;700&display=swap" rel="stylesheet">
<style>
  :root {
    --backdrop: #e4e5e7;
    --navy-deep: #21334f;
    --navy-soft: #6b7b8f;
    --ink: #25344d;
    --paper: #f1f1f2;
    --teal: #5fc0d6;
    --blue: #3f76bd;
    --icon-blue: #4a8fd0;
    --white: #ffffff;
  }
  * { margin: 0; padding: 0; box-sizing: border-box; }
  html, body {
    width: 1200px;
    height: 1200px;
    overflow: hidden;
    background: var(--backdrop);
    font-family: "Lexend", sans-serif;
  }
  .stage {
    position: relative;
    width: 1200px;
    height: 1200px;
  }
  .card {
    position: absolute;
    left: 250px;
    width: 700px;
    height: 400px;
    border-radius: 26px;
    overflow: hidden;
  }
  .card--front {
    top: 150px;
    background: linear-gradient(100deg, var(--navy-soft) 0%, #4b5d76 35%, var(--navy-deep) 75%);
    box-shadow: 0 4px 0 #0f1d33;
  }
  .card--back {
    top: 650px;
    background: var(--paper);
    box-shadow: 0 4px 0 #cfcfd1;
  }
  .wordmark {
    position: absolute;
    display: flex;
    align-items: center;
    gap: 16px;
    font-weight: 600;
    letter-spacing: 1px;
  }
  .wordmark__dot {
    border-radius: 50%;
    background: var(--icon-blue);
  }
  .card--front .wordmark {
    left: 50%;
    top: 50%;
    transform: translate(-50%, -50%);
    font-size: 62px;
    color: var(--white);
  }
  .card--front .wordmark__dot { width: 44px; height: 44px; }
  .card--back .wordmark {
    left: 64px;
    top: 62px;
    font-size: 40px;
    color: var(--ink);
  }
  .card--back .wordmark__dot { width: 30px; height: 30px; }
  .person {
    position: absolute;
    left: 380px;
    top: 150px;
  }
  .person__name {
    font-size: 34px;
    font-weight: 700;
    background: linear-gradient(90deg, var(--teal), var(--blue));
    -webkit-background-clip: text;
    background-clip: text;
    color: transparent;
    line-height: 1.1;
  }
  .person__title {
    font-size: 18px;
    color: var(--ink);
    margin-top: 4px;
  }
  .divider {
    position: absolute;
    left: 380px;
    right: 0;
    top: 238px;
    height: 2px;
    background: linear-gradient(90deg, var(--teal), var(--blue));
  }
  .office {
    position: absolute;
    left: 380px;
    top: 256px;
    color: var(--ink);
    font-size: 17px;
    line-height: 1.45;
  }
  .office__name { font-weight: 600; }
  .contacts {
    position: absolute;
    left: 120px;
    top: 262px;
    list-style: none;
    color: var(--ink);
    font-size: 17px;
  }
  .contacts li {
    display: flex;
    align-items: center;
    gap: 10px;
    line-height: 1.75;
  }
  .contacts svg { width: 16px; height: 16px; flex: none; }
</style>
</head>
<body>
<main class="stage">

  <section class="card card--front" aria-label="Card front">
    <div class="wordmark">
      <span class="wordmark__dot"></span>
      <span>VEROSTEL</span>
    </div>
  </section>

  <section class="card card--back" aria-label="Card back">
    <div class="wordmark">
      <span class="wordmark__dot"></span>
      <span>VEROSTEL</span>
    </div>

    <div class="person">
      <p class="person__name">Marek Halasz</p>
      <p class="person__title">Sales Representative</p>
    </div>

    <div class="divider"></div>

    <div class="office">
      <p class="office__name">Verostel Head Office</p>
      <p>Budapest XIII. Lenke utca 8.</p>
    </div>

    <ul class="contacts">
      <li>
        <svg viewBox="0 0 24 24" aria-hidden="true"><path fill="#4a8fd0" d="M6.6 10.8a15.1 15.1 0 0 0 6.6 6.6l2.2-2.2a1 1 0 0 1 1-.25 11.4 11.4 0 0 0 3.6.57 1 1 0 0 1 1 1V20a1 1 0 0 1-1 1A17 17 0 0 1 3 4a1 1 0 0 1 1-1h3.5a1 1 0 0 1 1 1c0 1.25.2 2.45.57 3.57a1 1 0 0 1-.25 1z"/></svg>
        <span>+36 30 412 7758</span>
      </li>
      <li>
        <svg viewBox="0 0 24 24" aria-hidden="true"><rect x="2" y="5" width="20" height="14" rx="1.5" fill="#4a8fd0"/><path d="M3 6l9 7 9-7" fill="none" stroke="#f1f1f2" stroke-width="1.6"/></svg>
        <span>szerviz@verostel.com</span>
      </li>
      <li>
        <svg viewBox="0 0 24 24" aria-hidden="true"><g fill="none" stroke="#4a8fd0" stroke-width="2"><circle cx="12" cy="12" r="9"/><ellipse cx="12" cy="12" rx="4" ry="9"/><path d="M3 12h18"/></g></svg>
        <span>www.verostel.com</span>
      </li>
    </ul>
  </section>

</main>
</body>
</html>
```